Boom Way Hoist Service Business Cards

I need a business card for "Boom Way Hoist and Haulage"

Boomway2023@hoistmail.net

Hoist Works LLC, Boom Way Hoist and Haulage LLC

555.014.7260 | www.BOOMWAYHOISTS.example

Harlow Falls & Ridgeport Regions

(IN) 14820 Maple Lane Harlow Falls, IN 46000

(OH) 2450 Pell Street Ridgeport, Ohio 44300

Colors
0094D4
00A9DD
6FCCEA
C7EBF8
E9F6FB
59FF00
82FF00
B8FF75
E3FFCB
F4FFEA
EE7325
F08F49
F5BC92
FAE3D3
FDF4ED
EB3D1F
EC4F4E
F09395
F8D3D4
FCEDEE
E54698
E96AAD
F1A4CE
F9D9EA
FCEFF6
A7469A
B969AE
D3A5CF
EDDBEB
F8F0F9

```html
<!DOCTYPE html>
<html lang="en">
<head>
<meta charset="utf-8">
<title>Boom Way Hoist and Haulage – Business Cards</title>
<link rel="stylesheet" href="https://fonts.googleapis.com/css2?family=Archivo+Black&family=Barlow:wght@500;600&display=swap">
<style>
  :root {
    --stage: #d4d1ca;
    --navy: #24245c;
    --red: #c8223c;
    --green: #43b649;
    --white: #ffffff;
    --panel: #f8f3f3;
    --panel-tint: #eeeef4;
    --ink: #111111;
  }
  html, body {
    margin: 0;
    width: 1200px;
    height: 1200px;
    overflow: hidden;
    background: var(--stage);
  }
  .sheet {
    position: relative;
    width: 1200px;
    height: 1200px;
  }
  .card {
    position: absolute;
    left: 221px;
    width: 745px;
    height: 425px;
    display: block;
  }
  .card-front { top: 144px; }
  .card-back { top: 626px; }
  .brand-name,
  .brand-tagline {
    font-family: "Archivo Black", sans-serif;
    fill: var(--white);
  }
  .contact {
    font-family: "Barlow", sans-serif;
    font-weight: 500;
    fill: var(--ink);
  }
  .contact-title {
    font-family: "Barlow", sans-serif;
    font-weight: 600;
    fill: var(--ink);
  }
</style>
</head>
<body>
<main class="sheet">

  <!-- Front of card -->
  <svg class="card card-front" viewBox="0 0 1100 628" aria-label="Business card front">
    <defs>
      <clipPath id="front-shape"><rect width="1100" height="628" rx="56"/></clipPath>
    </defs>
    <g clip-path="url(#front-shape)">
      <rect class="card-base" width="1100" height="628" fill="var(--navy)"/>
      <polygon class="band-red" points="360,0 1100,0 1100,140 820,628 60,628" fill="var(--red)"/>
      <polygon class="stripe-green-left" points="290,0 320,0 0,520 0,470" fill="var(--green)"/>
      <polygon class="stripe-green-left-thin" points="210,0 222,0 0,360 0,340" fill="var(--green)"/>
      <polygon class="stripe-green-right" points="1100,220 1100,270 895,628 865,628" fill="var(--green)"/>
      <polygon class="stripe-green-right-thin" points="1100,380 1100,400 1005,628 988,628" fill="var(--green)"/>
    </g>
    <text class="brand-name" x="830" y="318" text-anchor="end" font-size="96" letter-spacing="2">BOOM WAY</text>
    <text class="brand-tagline" x="830" y="384" text-anchor="end" font-size="25">HOIST &amp; HAULAGE</text>
    <text class="brand-tagline" x="830" y="420" text-anchor="end" font-size="25">SERVICES</text>
  </svg>

  <!-- Back of card -->
  <svg class="card card-back" viewBox="0 0 1100 628" aria-label="Business card back">
    <defs>
      <clipPath id="back-shape"><rect width="1100" height="628" rx="56"/></clipPath>
      <linearGradient id="fleet-tones" x1="0" y1="0" x2="1" y2="1">
        <stop offset="0" stop-color="#e2dede"/>
        <stop offset="0.45" stop-color="#9a9a9a"/>
        <stop offset="0.75" stop-color="#e8593a"/>
        <stop offset="1" stop-color="#43b649"/>
      </linearGradient>
    </defs>
    <g clip-path="url(#back-shape)">
      <rect class="card-base" width="1100" height="628" fill="var(--navy)"/>
      <polygon class="band-red" points="140,0 760,0 1100,420 1100,628 480,628" fill="var(--red)"/>
      <polygon class="stripe-green-top" points="820,0 860,0 1100,300 1100,350" fill="var(--green)"/>
      <polygon class="stripe-green-left" points="0,250 0,300 250,628 210,628" fill="var(--green)"/>
      <polygon class="stripe-green-left-thin" points="0,420 0,440 150,628 130,628" fill="var(--green)"/>
      <rect class="info-panel" x="46" y="37" width="1008" height="555" fill="var(--panel)"/>
      <polygon class="panel-tint" points="46,37 260,37 46,330" fill="var(--panel-tint)" opacity="0.8"/>
    </g>

    <text class="contact-title" x="91" y="150" font-size="24">Hoist Works LLC, Boom Way Hoist and Haulage LLC</text>
    <line class="divider" x1="92" y1="216" x2="620" y2="216" stroke="var(--ink)" stroke-width="1.5"/>
    <text class="contact" x="92" y="279" font-size="21">555.014.7260 | www.BOOMWAYHOISTS.example</text>
    <text class="contact" x="92" y="322" font-size="21">Harlow Falls &amp; Ridgeport Regions</text>
    <text class="contact" x="92" y="382" font-size="21">(IN) 14820 Maple Lane Harlow Falls, IN 46000</text>
    <text class="contact" x="92" y="423" font-size="21">(OH) 2450 Pell Street Ridgeport, Ohio 44300</text>
    <text class="contact" x="96" y="485" font-size="21">Boomway2023@hoistmail.net</text>

    <rect class="fleet-illustration" x="652" y="90" width="372" height="450" rx="6" fill="url(#fleet-tones)" opacity="0.85" role="img" aria-label="Illustration of a red boom truck and a green mobile crane in front of a building under construction"/>
  </svg>

</main>
</body>
</html>
```